US company needs luxury product packaging design for a line of hair extensions

What we Need:
Design product packaging for our top of the line hair extension product called Velorina™, the design should have the Velorina™ name,and the head from our Plumestrand logo on the box.

Who we are
Our company PlumeStrand™ is a wholesaler of 100% human hair extensions. We sell the best quality double drawn hair wefts, clip-ins and wigs.

The detailed brief is in the attached word document with examples of packaging we like and we have also uploaded our company logo

The winning designer(s) will work with us on 9 other products packages that we need, so it is important to think strategically

Thanks

Target Market(s)

African American Women

Industry/Entity Type

Hair And Beauty

Font styles to use
Serif
Decorative
Script

Colors
fbf289
b768aa
e24096
000000
fbd4d5
f59195
ffc214
d3a5cc
eda3c7

Requirements
Must have
• Evoke luxury
Nice to have
• See Attached brief

```html
<!DOCTYPE html>
<html lang="en">
<head>
<meta charset="utf-8">
<title>Velorina Hair Extension Packaging</title>
<link href="https://fonts.googleapis.com/css2?family=Josefin+Sans:wght@300&family=Questrial&display=swap" rel="stylesheet">
<style>
  :root {
    --stage: #e4e8eb;
    --stage-edge: #c9cfd4;
    --gold-light: #f0d98a;
    --amber: #e9a85a;
    --orange: #c8602e;
    --crimson: #8e1c1e;
    --maroon: #4a161e;
    --wine: #7a1618;
    --ink-light: #ffffff;
    --foil: #b08a2a;
  }
  html, body {
    margin: 0;
    padding: 0;
    width: 1200px;
    height: 1200px;
    overflow: hidden;
  }
  body {
    background: radial-gradient(ellipse at 50% 45%, #f1f3f4 0%, var(--stage) 55%, var(--stage-edge) 100%);
    position: relative;
  }
  .box-front {
    position: absolute;
    left: 300px;
    top: 150px;
    width: 600px;
    height: 900px;
    background:
      radial-gradient(ellipse 55% 18% at 55% 44%, rgba(200, 96, 46, 0.55), transparent 70%),
      radial-gradient(ellipse 45% 14% at 50% 63%, rgba(142, 28, 30, 0.6), transparent 70%),
      linear-gradient(180deg,
        var(--gold-light) 0%,
        var(--amber) 17%,
        var(--orange) 32%,
        var(--crimson) 47%,
        var(--wine) 60%,
        var(--maroon) 74%,
        var(--wine) 90%,
        var(--wine) 100%);
    box-shadow: 0 30px 60px rgba(0, 0, 0, 0.18);
  }
  .product-name {
    position: absolute;
    left: 0;
    right: 0;
    top: 425px;
    text-align: center;
    font-family: "Josefin Sans", "Questrial", sans-serif;
    font-weight: 300;
    font-size: 104px;
    line-height: 1;
    letter-spacing: -2px;
    color: var(--ink-light);
    margin: 0;
  }
  .product-name .mark {
    font-size: 22px;
    vertical-align: top;
    position: relative;
    top: -6px;
    letter-spacing: 0;
    margin-left: 2px;
  }
  .product-type {
    position: absolute;
    left: 0;
    right: 0;
    top: 545px;
    text-align: center;
    font-family: "Questrial", sans-serif;
    font-size: 30px;
    color: var(--ink-light);
    margin: 0;
  }
  .maker-sign {
    position: absolute;
    left: 0;
    right: 0;
    top: 795px;
    display: flex;
    justify-content: center;
    align-items: center;
    gap: 12px;
  }
  .maker-dot {
    width: 16px;
    height: 16px;
    border-radius: 50%;
    background: var(--foil);
  }
  .maker-name {
    font-family: "Questrial", sans-serif;
    font-size: 30px;
    color: var(--foil);
  }
</style>
</head>
<body>
  <section class="box-front" aria-label="Velorina hair extension box front">
    <h1 class="product-name">VELORINA<span class="mark">™</span></h1>
    <p class="product-type">Hair Extension</p>
    <div class="maker-sign">
      <span class="maker-dot"></span>
      <span class="maker-name">Plumestrand</span>
    </div>
  </section>
</body>
</html>
```